TARPLOAD business card design

TARPLOAD is a manufacturer of skip bags supplying both the domestic and commercial market. We wish to convey core characteristics of strength, professionalism and reliability to our customers. We are after a business card that uses our company colours of black and yellow as well as incorporating our logo. Our customers are predominantly in the construction or hardware industry. It is important the cards are professional as we are a small company wishing to appear larger than we actually are. more info on the company and product available at www.tarpload-example.com.au

Target Market(s)

hardware buyers, contruction company owners

Industry/Entity Type

Construction

Requirements
Must have
• company colours of black and yellow - No other colours or variation of yellow black. our company logo. card design must convey "tough"
• Card design must be landscape
• Details to be included on the card are:
• Name and Tiltle
• Phone number : 1300 41 62 53
• Mobile: 0452 718 903
• Fax: 03 9617 4852
• email: dale.hendry@tarpload-example.com.au
• address: PO Box 517, Kelvindale, VIC,3294
• Text in white when on a black background
Nice to have
• I like the idea of the back of the card being black with lighter circle area in the middle with black logo in the centre. Similar to the attached "iconic" card

```html
<!DOCTYPE html>
<html lang="en">
<head>
<meta charset="utf-8">
<title>TARPLOAD Business Card</title>
<link rel="stylesheet" href="https://fonts.googleapis.com/css2?family=Open+Sans:wght@400;700&family=Syncopate:wght@700&display=swap">
<style>
  :root {
    --card-black: #000000;
    --card-yellow: #ebcf00;
    --page-white: #ffffff;
    --edge: #1a1a2e;
  }
  html, body {
    margin: 0;
    padding: 0;
    width: 991px;
    height: 1200px;
    overflow: hidden;
    background: var(--page-white);
  }
  .sheet {
    position: relative;
    width: 991px;
    height: 1200px;
  }
  .card-back {
    position: absolute;
    left: 0;
    top: 0;
    width: 991px;
    height: 576px;
    background: var(--card-black);
  }
  .back-disc {
    position: absolute;
    left: 294px;
    top: 60px;
    width: 456px;
    height: 456px;
    border-radius: 50%;
    background: var(--card-yellow);
    display: flex;
    align-items: center;
    justify-content: center;
  }
  .brand-name {
    font-family: "Open Sans", Arial, sans-serif;
    font-weight: 700;
    color: var(--card-black);
    letter-spacing: 1px;
    line-height: 1;
    margin: 0;
  }
  .back-disc .brand-name {
    font-size: 66px;
  }
  .card-front {
    position: absolute;
    left: 0;
    top: 623px;
    width: 989px;
    height: 575px;
    background: var(--card-yellow);
    border: 1px solid var(--edge);
    text-align: center;
    font-family: "Open Sans", Arial, sans-serif;
    color: var(--card-black);
  }
  .front-brand {
    position: absolute;
    left: 0;
    right: 0;
    top: 155px;
    display: flex;
    justify-content: center;
  }
  .front-brand .brand-name {
    font-size: 32px;
  }
  .person-name {
    position: absolute;
    left: 0;
    right: 0;
    top: 290px;
    margin: 0;
    font-family: "Syncopate", Arial, sans-serif;
    font-weight: 700;
    font-size: 34px;
    letter-spacing: -1px;
    line-height: 1;
  }
  .person-title {
    position: absolute;
    left: 0;
    right: 0;
    top: 339px;
    margin: 0;
    font-size: 17px;
    letter-spacing: 1px;
    line-height: 1;
  }
  .contact {
    position: absolute;
    left: 0;
    right: 0;
    top: 446px;
    margin: 0;
    font-weight: 700;
    font-size: 21px;
    line-height: 28px;
    letter-spacing: 0.5px;
  }
  .contact .phones {
    display: block;
    margin-top: 12px;
  }
</style>
</head>
<body>
<div class="sheet">
  <section class="card-back">
    <div class="back-disc">
      <p class="brand-name">TARPLOAD</p>
    </div>
  </section>

  <section class="card-front">
    <div class="front-brand">
      <p class="brand-name">TARPLOAD</p>
    </div>
    <h1 class="person-name">DALE HENDRY</h1>
    <p class="person-title">MANAGING&nbsp; DIRECTOR</p>
    <p class="contact">
      e:&nbsp; dale.hendry@tarpload-example.com.au<br>
      a: PO Box 517, Kelvindale, VIC,3294
      <span class="phones">p: 1300 41 62 53 | m: 0452 718 903 | f: 03 9617 4852</span>
    </p>
  </section>
</div>
</body>
</html>
```